Looking for an Innovative Print Design (Service Directory)

We need a new design for our advertisement within a printed colour services directory.

We are a compensation law firm called Velbrook Compensation Lawyers. Feel free to take a browse of our website www.velbrooklegal.com.au to get an idea of what we do and the kind of firm we are.

We are in the process of redeveloping our website and as such, so please don't adhere to the design principles of the current site- impress us with your originality!

On top of any editable formats, your final submissions must include a .pdf copy.
The same design will need to be presented in two dimensions:

- 154mm x 118mm (B1/B2 Half Page);
- 175mm x 113mm (B4 Half Page).

[For more information refer to attached Pdf.]

We have attached for you a few examples of other firms' designs (Sample1,2,3). These are by no means good, or what we're after, it's just to provide you with an idea of what sort of advertisements go into the service directory.

Hi all,

We want to emphasise that a priority of the design is that it must look:
• Professional
• Sophisticated
Please do not hesitate to use completely different colour schemes to the ones that are on our website- as we have said, our website will change in the near future, so cohesion between the current project and the website is not necessary!

Thanks!

Thank you for your submissions so far. There are some great ideas hidden in there. 

An issue we are having is that most of you are conforming to the same understanding of what it should look like. Remember that there is NO NEED to be bound by the image of firm as is. That is, feel free to use a different colour logo.

For inspiration, we relate well to the design aesthetics of: http://www.tinfernstudio.co.uk/

Look forward to seeing your 'out of the box' submissions. 

Reason: We've received a large amount of fantastic designs. However, what we're really looking for is something original. Please feel free to think outside the box (the final design doesn't need to look like a print ad), and construct a design that is completely incongruous with our website! While we do appreciate a minimalistic design, we have yet to receive something that really grabs your attention with its visuals. We're not sure but this may or may not be achieved with a full colour design. Thanks for all your submissions- they all have some features that really click with us. We look forward to the next wave of submissions!

Target Market(s)

We have various target markets, including mainly families, elderly people, blue collar workers.

These are individuals who are looking for assistance. They feel helpless or wronged.

Keep in mind that the people accessing these are those who prefer going to a printed directory rather than using a google search.

Industry/Entity Type

Law Firm

Font styles to use
Serif
Sans Serif

Requirements
Must have
• - Our name 'Velbrook Compensation Lawyers'
- Our logo (attached as logo.eps, logo.png, and logo.tif)
- Must include phone number as 1300 XXX XXX (this must be prominent)
- Must include the following service areas in these words: Motor vehicle claims, medical claims, superannuation claims, Workplace claims, negligence claims
- Our email address: info@velbrooklegal.com.au
- Our website address: www.velbrooklegal.com.au
- The following catchphrases: '98% success rate', and 'No win no fee' in those words
- Our location '412 Carvel Lane, Tarrowdale, NEWHAVEN'
- For sizing dimensions, we need one in 154mm x 118mm and also a design in 175mm x 113mm (B4 Half Page) [refer to pdf attached]
Nice to have
• - Text indicating free initial consulatation
- Professional colour scheme
- As our website will be changed, do not worry about making the advertisement cohesive with our website design
- We want the design to be modern, but still professional
- Clean typeface
- No gradient colour scheme
- When designing, if you are looking to place more text onto the advertisement, these may be some considerations (feel free to change the wording): Accredited specialists, home and hospital visits

```html
<!DOCTYPE html>
<html lang="en">
<head>
<meta charset="utf-8">
<title>Velbrook Compensation Lawyers – Directory Advertisement</title>
<link rel="stylesheet" href="https://fonts.googleapis.com/css2?family=Lato:wght@300;400&family=Open+Sans:ital,wght@0,700;1,700&display=swap">
<style>
  :root {
    --page: #ffffff;
    --stone: #e8e7e5;
    --charcoal: #414740;
    --ember: #e96b3c;
    --brand-orange: #e8651a;
    --ink: #3a3d3a;
    --muted: #9a968f;
    --muted-dark: #8f8e89;
    --white: #ffffff;
    --caption: #c6c5cb;
  }
  html, body {
    margin: 0;
    padding: 0;
    width: 1200px;
    height: 1000px;
    overflow: hidden;
    background: var(--page);
  }
  .canvas {
    position: relative;
    width: 1200px;
    height: 1000px;
  }
  .ad {
    position: absolute;
    left: 68px;
    top: 25px;
    width: 1066px;
    height: 817px;
  }
  .ad-shapes {
    position: absolute;
    inset: 0;
    filter: drop-shadow(4px 6px 6px rgba(0,0,0,0.35));
  }
  .ad-text {
    position: absolute;
    margin: 0;
    text-align: center;
  }
  .brand {
    position: absolute;
    left: 36px;
    top: 47px;
    display: flex;
    align-items: center;
    gap: 30px;
  }
  .brand-mark {
    width: 116px;
    height: 116px;
    border-radius: 50%;
    background: var(--brand-orange);
  }
  .brand-name {
    font-family: "Lato", sans-serif;
    font-weight: 400;
    color: var(--ink);
    line-height: 1;
  }
  .brand-name .primary {
    display: block;
    font-size: 62px;
    letter-spacing: 5px;
  }
  .brand-name .secondary {
    display: block;
    font-size: 19px;
    letter-spacing: 5.6px;
    margin-top: 10px;
  }
  .headline {
    left: 608px;
    width: 458px;
    top: 28px;
    font-family: "Open Sans", sans-serif;
    font-style: italic;
    font-weight: 700;
    font-size: 78px;
    line-height: 84px;
    letter-spacing: 2px;
    color: var(--muted);
  }
  .success {
    left: 608px;
    width: 458px;
    top: 220px;
    font-family: "Open Sans", sans-serif;
    font-style: italic;
    font-weight: 700;
    font-size: 28px;
    letter-spacing: 1.6px;
    color: var(--muted);
  }
  .services {
    left: 40px;
    width: 494px;
    top: 195px;
    list-style: none;
    padding: 0;
    font-family: "Lato", sans-serif;
    font-weight: 400;
    font-size: 33px;
    line-height: 59px;
    color: var(--ink);
  }
  .credentials {
    left: 0;
    width: 380px;
    top: 617px;
    font-family: "Open Sans", sans-serif;
    font-style: italic;
    font-weight: 700;
    font-size: 29px;
    line-height: 35px;
    letter-spacing: 2px;
    color: var(--muted-dark);
  }
  .credentials span { display: block; }
  .credentials .gap { margin-top: 27px; }
  .offer {
    left: 514px;
    width: 460px;
    top: 432px;
    font-family: "Lato", sans-serif;
    font-weight: 300;
    font-size: 40px;
    line-height: 42px;
    letter-spacing: 0.8px;
    color: var(--white);
  }
  .phone {
    left: 470px;
    width: 550px;
    top: 550px;
    font-family: "Open Sans", sans-serif;
    font-weight: 700;
    font-size: 66px;
    letter-spacing: 2px;
    color: var(--white);
  }
  .contact {
    left: 460px;
    width: 570px;
    top: 673px;
    font-family: "Lato", sans-serif;
    font-weight: 300;
    font-style: normal;
    font-size: 28px;
    line-height: 39px;
    letter-spacing: 0.8px;
    color: var(--white);
  }
  .contact span { display: block; }
  .size-label {
    position: absolute;
    left: 0;
    width: 1180px;
    top: 880px;
    margin: 0;
    text-align: center;
    font-family: "Open Sans", sans-serif;
    font-weight: 700;
    font-size: 58px;
    color: var(--caption);
  }
</style>
</head>
<body>
<div class="canvas">
  <section class="ad" aria-label="Velbrook Compensation Lawyers advertisement">
    <svg class="ad-shapes" width="1066" height="817" viewBox="0 0 1066 817" aria-hidden="true">
      <rect width="1066" height="817" fill="var(--stone)"/>
      <polygon points="663,305 1066,305 1066,817 0,817 0,576 346,576" fill="var(--white)"/>
      <polygon points="668,309 1066,309 1066,817 0,817 0,580 351,580" fill="var(--ember)"/>
      <rect x="604" y="0" width="462" height="305" fill="var(--white)"/>
      <rect x="608" y="0" width="458" height="301" fill="var(--charcoal)"/>
      <rect x="0" y="578" width="394" height="239" fill="var(--white)"/>
      <rect x="0" y="582" width="390" height="235" fill="var(--charcoal)"/>
    </svg>

    <div class="brand">
      <div class="brand-mark" aria-hidden="true"></div>
      <div class="brand-name">
        <span class="primary">VELBROOK</span>
        <span class="secondary">COMPENSATION LAWYERS</span>
      </div>
    </div>

    <h1 class="ad-text headline">NO WIN<br>NO FEE</h1>
    <p class="ad-text success">98% SUCCESS RATE</p>

    <ul class="ad-text services">
      <li>Motor vehicle claims</li>
      <li>Medical claims</li>
      <li>Superannuation claims</li>
      <li>Workplace claims</li>
      <li>Negligence claims</li>
    </ul>

    <p class="ad-text credentials">
      <span>ACCREDITED</span>
      <span>SPECIALISTS</span>
      <span class="gap">HOME AND</span>
      <span>HOSPITAL VISITS</span>
    </p>

    <p class="ad-text offer">FREE INITIAL<br>CONSULATATION</p>
    <p class="ad-text phone">1300.246.1357</p>
    <address class="ad-text contact">
      <span>info@velbrooklegal.com.au</span>
      <span>www.velbrooklegal.com.au</span>
      <span>412 Carvel Lane, Tarrowdale, NEWHAVEN</span>
    </address>
  </section>

  <p class="size-label">AD 154mm x 118mm</p>
</div>
</body>
</html>
```